Larkspur Ridge Management - Business Cards

I need business cards. My current logo was designed by a designer at this site and I very much like and am happy with the results. I would like a business card that is trendy, unique, current yet professional. I deal with high net worth clients daily

Target Market(s)

Out of state investors looking to get into the rental market in Ohio

Industry/Entity Type

Property Management, Consulting

Contact Information for Business Card

Name, Title (Chief Financial Officer) office phone number (555) 817-3094 website address larkridgemgmt.example

Font styles to use
Sans Serif

Colors
0054AA
0677BA
7BADD7
CADEEF
E8F1F8
0094D4
00A9DD
6FCCEA
C7EBF8
E9F6FB
00AB8E
00BBA5
67D7C9
C6EFE9
E9F9F6

```html
<!DOCTYPE html>
<html lang="en">
<head>
<meta charset="utf-8">
<title>Larkspur Ridge Management – Business Cards</title>
<link href="https://fonts.googleapis.com/css2?family=Montserrat:wght@500&family=Roboto:wght@400;700&family=Open+Sans:wght@600&display=swap" rel="stylesheet">
<style>
  :root {
    --backdrop: #2b2b2b;
    --card-light: #f1f1f1;
    --card-shade: #dedede;
    --navy: #1f2f57;
    --red: #c0232a;
    --grey-text: #555b63;
  }
  * { margin: 0; padding: 0; box-sizing: border-box; }
  html, body { width: 1200px; height: 1138px; overflow: hidden; }
  body { background: var(--backdrop); position: relative; font-family: "Roboto", sans-serif; }

  .card {
    position: absolute;
    left: 290px;
    width: 620px;
    height: 374px;
    border-radius: 16px;
    overflow: hidden;
    background: linear-gradient(160deg, var(--card-light) 0%, #ececec 55%, var(--card-shade) 100%);
  }
  .card--front { top: 186px; }
  .card--back  { top: 608px; }

  .brand-name {
    position: absolute;
    display: flex;
    align-items: center;
    gap: 12px;
    color: var(--navy);
    font-family: "Roboto", sans-serif;
    font-weight: 700;
    line-height: 1.15;
  }
  .brand-name .brand-square {
    flex: none;
    background: var(--navy);
  }
  .card--front .brand-name {
    left: 0; right: 0; top: 130px;
    justify-content: center;
    font-size: 30px;
  }
  .card--front .brand-square { width: 30px; height: 30px; }

  .front-web {
    position: absolute;
    left: 0; right: 0; top: 334px;
    text-align: center;
    font-family: "Montserrat", sans-serif;
    font-weight: 500;
    font-size: 16px;
    letter-spacing: 4.5px;
    color: var(--navy);
  }

  .card--back .brand-name {
    left: 36px; top: 134px; width: 270px;
    font-size: 26px;
  }
  .card--back .brand-square { width: 26px; height: 26px; }

  .contact { position: absolute; left: 352px; top: 76px; color: var(--navy); }
  .contact-name {
    font-family: "Open Sans", sans-serif;
    font-weight: 600;
    font-size: 25px;
    color: var(--red);
    line-height: 1.1;
  }
  .contact-title { font-size: 16px; color: var(--grey-text); margin-top: 2px; }
  .contact-address { font-size: 15.5px; line-height: 23px; margin-top: 18px; }
  .contact-list { list-style: none; margin-top: 12px; font-size: 15.5px; }
  .contact-list li { display: flex; align-items: center; height: 22px; }
  .contact-list svg { width: 15px; height: 15px; margin-right: 14px; fill: var(--red); }

  .band-red {
    position: absolute; left: 0; bottom: 0;
    width: 280px; height: 14px;
    background: var(--red);
  }
  .band-navy {
    position: absolute; right: 0; bottom: 0;
    width: 356px; height: 46px;
    background: var(--navy);
    clip-path: polygon(30px 0, 100% 0, 100% 100%, 0 100%);
    color: #fff;
    font-size: 16px;
    display: flex; align-items: center;
    padding-left: 86px;
  }
</style>
</head>
<body>

  <section class="card card--front">
    <div class="brand-name"><span class="brand-square"></span>Larkspur Ridge Management</div>
    <div class="front-web">www.larkridgemgmt.example</div>
  </section>

  <section class="card card--back">
    <div class="brand-name"><span class="brand-square"></span>Larkspur Ridge Management</div>

    <div class="contact">
      <div class="contact-name">Daniel Whitcombe</div>
      <div class="contact-title">Chief Financial Officer</div>
      <div class="contact-address">Street No 000, Bldg No. 0,<br>Country State - 000000</div>
      <ul class="contact-list">
        <li>
          <svg viewBox="0 0 16 16" aria-hidden="true"><path d="M2 5c0-2 3-3 6-3s6 1 6 3v1.5h-3V5H5v1.5H2z"/><path d="M4 7h8l2 7H2z"/></svg>
          (555) 817-3094
        </li>
        <li>
          <svg viewBox="0 0 16 16" aria-hidden="true"><path d="M1 3h14v10H1z M2.5 4.5 8 9l5.5-4.5v-0.2h-11z" fill-rule="evenodd"/></svg>
          www.larkridgemgmt.example
        </li>
        <li>
          <svg viewBox="0 0 16 16" aria-hidden="true"><path d="M8 1a7 7 0 1 0 0 14A7 7 0 0 0 8 1zm0 1.5c1 1.2 1.6 3 1.7 4.7H6.3C6.4 5.5 7 3.7 8 2.5zM2.6 7.2a5.5 5.5 0 0 1 2.7-4c-.6 1.2-1 2.6-1 4zm0 1.6h1.7c0 1.4.4 2.8 1 4a5.5 5.5 0 0 1-2.7-4zM8 13.5c-1-1.2-1.6-3-1.7-4.7h3.4c-.1 1.7-.7 3.5-1.7 4.7zm2.7-.7c.6-1.2 1-2.6 1-4h1.7a5.5 5.5 0 0 1-2.7 4zm1-5.6c0-1.4-.4-2.8-1-4a5.5 5.5 0 0 1 2.7 4z"/></svg>
          info@larkridgemgmt.example
        </li>
      </ul>
    </div>

    <div class="band-red"></div>
    <div class="band-navy">Larkspur Ridge Management</div>
  </section>

</body>
</html>
```